drink bottle label

Our drink is called VELTRANA qa, a 2000 year old Asian formula for a fermented green tea drink. Flavored with organic ginger juice, cinnamon and lime. Very tasty and refreshing, good for sports recovery, digestion,liver detox,overall health and vitality. Naturally fermented creating a- no sugar, low GI, salt,-fat and gluten free- fizzy drink alternative to soft drink, sports drinks or beer. The bottle is a brown 330ml long neck bottle. For the diet and health conscious individual. We would like the label to be upmarket for restaurants & trendy organic food suppliers.
Updates

The bottle is brown. Try using black-gold-silver-white for the subject in a white or silver border

Target Market(s)

Upmarket, for restaurant & trendy organic food supplies.Sophisticated Health conscious people who don't want high sugar, caffeine drinks.

Industry/Entity Type

Health

Requirements
Must have
• The drink name and registered brand is" VELTRANA qa."
Must feature PROBIOTICS & ENZYMES for detox.No artificial preservatives or colours. 100% Organic & raw living culture.Low GI low calorie- no cane sugar, no salt-
- no lactose, Coeliac -diabetic & vegan friendly. Ginger Brew.
Nice to have
• tastes great-revitalize- 330ml brown bottle

```html
<!DOCTYPE html>
<html lang="en">
<head>
<meta charset="utf-8">
<title>VELTRANA qa. – Drink Label</title>
<link href="https://fonts.googleapis.com/css2?family=Archivo+Black&family=Tinos:wght@400&display=swap" rel="stylesheet">
<style>
  :root {
    --frame: #e3e3e3;
    --gold: #f1bb00;
    --gold-deep: #e6ad00;
    --sun: #ee9a00;
    --glass: #f4c43a;
    --brand: #3d3d3d;
    --ink: #1a1a1a;
  }
  html, body {
    margin: 0;
    padding: 0;
    width: 1200px;
    height: 635px;
    overflow: hidden;
    background: var(--frame);
  }
  .label {
    position: absolute;
    left: 10px;
    top: 10px;
    width: 1170px;
    height: 615px;
    background: var(--gold);
    overflow: hidden;
  }
  .field-art {
    position: absolute;
    left: 0;
    bottom: 0;
    width: 100%;
    height: 330px;
    background: linear-gradient(to top, rgba(190, 140, 0, 0.28), rgba(190, 140, 0, 0));
  }
  .sun-badge {
    position: absolute;
    left: 380px;
    top: -10px;
    width: 334px;
    height: 334px;
  }
  .brand-name {
    position: absolute;
    left: 0;
    width: 1140px;
    text-align: center;
    font-family: "Archivo Black", "Arial Black", sans-serif;
    color: var(--brand);
    line-height: 1;
    margin: 0;
  }
  .brand-name .word {
    display: block;
  }
  .brand-name .word-main {
    font-size: 92px;
    position: absolute;
    top: 400px;
    left: 0;
    width: 100%;
    letter-spacing: 1px;
  }
  .brand-name .word-sub {
    font-size: 110px;
    position: absolute;
    top: 490px;
    left: 0;
    width: 100%;
  }
  .claims {
    position: absolute;
    right: 28px;
    top: 384px;
    margin: 0;
    text-align: right;
    font-family: "Tinos", "Times New Roman", serif;
    font-size: 15px;
    line-height: 20px;
    color: var(--ink);
  }
  .claims p {
    margin: 0 0 22px 0;
  }
  .claims p:last-child {
    margin-bottom: 0;
  }
</style>
</head>
<body>
  <main class="label">
    <div class="field-art" role="img" aria-label="Faint illustration of wheat and grass stalks rising from the bottom of the label"></div>

    <svg class="sun-badge" viewBox="0 0 334 334" xmlns="http://www.w3.org/2000/svg">
      <circle cx="167" cy="167" r="167" fill="var(--sun)"/>
      <g role="img" aria-label="Illustration of a glass of drink with a lime slice on the rim">
        <rect x="92" y="70" width="150" height="190" rx="20" fill="var(--glass)" opacity="0.55"/>
      </g>
    </svg>

    <h1 class="brand-name">
      <span class="word word-main">VELTRANA</span>
      <span class="word word-sub">qa.</span>
    </h1>

    <section class="claims">
      <p>PROBIOTICS &amp; ENZYMES for detox.</p>
      <p>No artificial preservatives or colours<br>100% Organic &amp; raw living culture</p>
      <p>Low GI - low calorie<br>No cane sugar - no salt - no lactose<br>Coeliac - diabetic &amp; vegan friendly</p>
      <p>Ginger Brew</p>
    </section>
  </main>
</body>
</html>
```